5 Email Newsletter Templates Needed

We need 5 email templates for our email marketing campaign. We are an Insurance Agency in Los Angeles called KPT-Silverbrook Insurance Services. We use Mailvance Hub as our email marketing platform. The templates need to be simple, a nice header, not to busy and you will need to use our color palette. The first email template we need is for our current clients / prospects. The content we will put in this email will be insurance tips and information, short and simple about 2 small paragraphs. The next 3 templates all need to be the same but different colors. One red, one yellow and one green. These will be alerts from kpt-silverbrook. An example a major earthquake hits we will send a red alert. A legislative change on healthcare and we send a yellow alert. We buy another location and we send a green alert. The last email is for our COINs (Centers of Influence, the people who refer business to us). I uploaded an email from one of our business consultants to give an idea of the size and sophistication we are looking for. I also uploaded our corporate brochure and color palette so you can learn more about our firm.

Target Market(s)

Our target markets are commercial business 1mm plus in revenue, 500 employees, high net worth individuals. Our COINs are CPAs, CFOs, Business Managers

Requirements
Nice to have
• HTML Code is desired. You can also provide just an image file for the header and our email marketing program will do the coding for us.
Should not have
• No cartoon looking graphics. Do not use old-style fonts like Times New Roman.

```html
<!DOCTYPE html>
<html lang="en">
<head>
<meta charset="utf-8">
<title>KPT-Silverbrook Newsletter No12</title>
<link rel="stylesheet" href="https://fonts.googleapis.com/css2?family=Arimo:wght@400;700&display=swap">
<style>
  :root {
    --page-teal: #0d5e80;
    --card-grey: #cfcfcb;
    --ear-taupe: #a9a49c;
    --header-white: #ffffff;
    --brand-blue: #145f82;
    --brand-green: #0f6b4f;
    --text-dark: #333333;
    --text-heading: #3a3a3a;
    --link-orange: #d9731a;
    --rule-grey: #8e8c88;
    --photo-dark: #2a2a2c;
    --photo-warm: #6b5a50;
  }
  * { box-sizing: border-box; margin: 0; padding: 0; }
  html, body {
    width: 884px; height: 1200px; overflow: hidden;
    background: var(--page-teal);
    font-family: "Arimo", Arial, sans-serif;
    color: var(--text-dark);
  }
  .newsletter { position: relative; width: 884px; height: 1200px; }
  .card {
    position: absolute; left: 62px; top: 29px; width: 760px; height: 1138px;
    background: var(--card-grey); border-radius: 14px;
  }
  .ear {
    position: absolute; top: 70px; width: 30px; height: 40px;
    background: var(--ear-taupe); border-radius: 12px 12px 0 0;
  }
  .ear-left { left: 47px; }
  .ear-right { left: 809px; }
  .topline {
    position: absolute; left: 105px; right: 102px; top: 69px;
    display: flex; justify-content: space-between; align-items: center;
    font-size: 12.5px; color: var(--text-dark);
  }
  .share { display: flex; align-items: center; gap: 6px; }
  .share-icon { width: 12px; height: 12px; background: #555; border-radius: 2px; }
  .masthead {
    position: absolute; left: 47px; top: 99px; width: 792px; height: 118px;
    background: var(--header-white); border-radius: 14px;
  }
  .brand {
    position: absolute; left: 58px; top: 26px;
    display: flex; align-items: center; gap: 12px;
  }
  .brand-square { width: 30px; height: 30px; background: var(--brand-green); }
  .brand-name {
    font-size: 27px; font-weight: 700; color: var(--brand-green); line-height: 1.1;
  }
  .brand-name small { display: block; font-size: 27px; }
  .issue-number {
    position: absolute; right: 56px; top: 32px;
    font-size: 50px; font-weight: 700; color: var(--brand-blue); letter-spacing: -1px;
  }
  .rule {
    position: absolute; left: 105px; width: 676px; top: 250px; height: 7px;
    border-top: 3px solid var(--rule-grey); border-bottom: 2px solid var(--rule-grey);
  }
  .hero-photo {
    position: absolute; left: 105px; top: 273px; width: 676px; height: 312px;
    background: radial-gradient(ellipse at 50% 55%, var(--photo-warm) 0%, var(--photo-dark) 70%);
  }
  .content { position: absolute; left: 105px; width: 676px; }
  .intro { top: 616px; font-size: 16px; line-height: 26.5px; }
  .intro strong { font-size: 19px; }
  .section-title {
    top: 772px; font-size: 17.5px; font-weight: 700; color: var(--text-heading);
  }
  .section-body { top: 801px; font-size: 16px; line-height: 26.5px; }
  .footer-note { top: 1006px; font-size: 14px; line-height: 26px; }
  .footer-links { top: 1084px; font-size: 14px; line-height: 26px; }
  .footer-links a, .footer-note a { color: var(--link-orange); text-decoration: none; }
  .sep { color: #9a9a9a; margin: 0 3px; }
</style>
</head>
<body>
<div class="newsletter">
  <div class="ear ear-left"></div>
  <div class="ear ear-right"></div>
  <div class="card"></div>

  <div class="topline">
    <span class="share">Share this on Chirpnet <span class="share-icon"></span></span>
    <span>February 2011</span>
  </div>

  <header class="masthead">
    <div class="brand">
      <div class="brand-square"></div>
      <div class="brand-name">KPT-Silverbrook<small>Insurance Services, LLC</small></div>
    </div>
    <div class="issue-number">№12</div>
  </header>

  <div class="rule"></div>

  <div class="hero-photo" role="img" aria-label="Photo of a smiling group of business people looking up at the camera"></div>

  <p class="content intro"><strong>Risk.</strong> There is no opportunity without it. How much or how little you choose to expose yourself to, however, is up to you. KPT-Silverbrook Insurance Services provides the tools, information and expert guidance you need to choose wisely. Because you never know when opportunity will knock … or what risks it may bring. With KPT-Silverbrook, you can be ready for anything.</p>

  <h2 class="content section-title">EXPERIENCE, INNOVATION, COMMITMENT: EXPECT MORE.</h2>
  <p class="content section-body">The world was a very different place in1933, when the company that would one day become KPT-Silverbrook Insurance Services was founded. Simpler. Safer. And more insular. But as times changed and the insurance industry evolved, so did KPT-Silverbrook.</p>

  <p class="content footer-note">You're receiving this newsletter because you've subscribed to the KPT Silverbrook<br>Not interested anymore? <a href="#">Unsubscribe.</a></p>

  <p class="content footer-links">
    <a href="#">Join Our Newsletter</a><span class="sep">|</span><a href="#">Share this with a Friend</a><span class="sep">|</span><a href="#">Stop Future Mailings</a><span class="sep">|</span><a href="#">Update Your Profile</a><br>
    Copyright © 2011 KPT Silverbrook. All rights reserved.
  </p>
</div>
</body>
</html>
```